依頼詳細
■ 重視する点/検討基準

以下のポイントを重視して選択させて頂きます。

・新聞折込チラシでの問い合わせアップにつながる新しさと信頼感
・サービスの特徴がわかりやすい
・高齢者の方にも読みやすい
・高齢でスマートフォン操作に慣れていない方にも、HPにアクセスしやすい構成
記載項目
■ 入れて欲しい内容
・有効期限
・通常価格25,000円が今だけ税込5000円
・見積もり費用や出張費用、その他の追加料金がかからないこと
・お家一軒丸ごとが洗浄範囲であること
・会社情報とHPにつながるQRの記載欄、集計のためのチラシ識別番号欄があること

※会社情報やロゴはこちらで入れるので、どこに何を配置するかわかるようにアテで入れていただけますと幸いです。
サイズ
B4
ページ数
片面
希望イメージ
シンプル 複雑
単色 カラフル
暗い 明るい
日常 高級
遊び心 厳粛
未来的 伝統的
女性的 男性的
希望する色
納品ファイル
• イラストレーター形式 (.ai)
補足説明
確認用のPDFデータと、文字編集可能なイラストレータデータでの納品をお願いいたします。

チラシデータは今後ターゲットや内容を変えて配布する予定ですので、二次利用があります。
【追記 締め切りを延長いたしました】
排水管洗浄のイメージを変えたいです。
従来の排水管チラシやネットにあるような形ではなく、新しい+αのアイデアを採用いたします。

シニアの方がターゲットなので、読みやすく分かりやすいデザインを希望いたします。
■ 選んだ理由

排水管洗浄をイメージやすいイラスト、写真の使い方や、綺麗な文字の組み方が素敵でした。
施工後に水回りのトラブルが解決し、綺麗になるのがイメージしやすかったです。

■ 提案者全員のお礼・コメント

提出いただいた2パターンとも、今までになかった見せ方と信頼感がありました。
素敵なご提案をいただき、弊社の社員一同、大変喜んでおります。
ありがとうございました。

```html
<!DOCTYPE html>
<html lang="ja">
<head>
<meta charset="UTF-8">
<title>排水管お掃除キャンペーン チラシ</title>
<link href="https://fonts.googleapis.com/css2?family=Noto+Sans+JP:wght@400;500;700;900&display=swap" rel="stylesheet">
<style>
:root{
  --blue:#1d9ad8;
  --blue-dark:#0d5fa8;
  --navy:#0b3f7a;
  --sky:#dff1fb;
  --yellow:#ffe600;
  --pink:#e63c78;
  --orange:#f39200;
  --ink:#1a1a1a;
  --white:#ffffff;
  --gray:#6b7480;
}
*{margin:0;padding:0;box-sizing:border-box}
html,body{width:846px;height:1200px;overflow:hidden;background:#fff}
body{font-family:"Noto Sans JP",sans-serif;color:var(--ink)}
.flyer{position:relative;width:846px;height:1200px;overflow:hidden;background:var(--white)}
.abs{position:absolute}

/* header */
.hero-photo{left:430px;top:0;width:416px;height:240px;background:linear-gradient(160deg,#f1f3f5,#d9dee3 60%,#c9ced4)}
.worries{left:28px;top:28px;display:flex;flex-direction:column;gap:12px}
.worry{background:var(--sky);color:var(--navy);font-weight:700;font-size:24px;padding:8px 22px;border-radius:30px;width:fit-content}
.worry:nth-child(2){margin-left:18px}
.worry:nth-child(3){margin-left:6px}

.headline-band{left:0;top:240px;width:846px;height:140px;background:var(--yellow)}
.tag-smell{left:40px;top:252px;background:var(--ink);color:var(--yellow);font-weight:900;font-size:28px;line-height:1.3;padding:2px 16px}
.headline{left:40px;top:292px;font-weight:900;font-size:62px;line-height:1.2;letter-spacing:2px;color:var(--ink);white-space:nowrap}
.headline .dirty{display:inline-block;background:var(--white);color:var(--pink);border-radius:50%;padding:0 14px;font-size:70px;line-height:1.1}
.headline-sub{left:670px;top:346px;font-weight:700;font-size:18px;line-height:1.3;white-space:nowrap}

/* campaign */
.campaign{left:0;top:380px;width:846px;height:300px;background:var(--blue)}
.campaign-banner{left:60px;top:392px;width:726px;height:38px;background:var(--navy);color:var(--white);font-weight:700;font-size:23px;text-align:center;line-height:38px;border-radius:4px}
.campaign-pill{left:110px;top:438px;width:626px;height:54px;background:var(--white);border-radius:30px;color:var(--pink);font-weight:900;font-size:34px;text-align:center;line-height:54px}
.price-panel{left:20px;top:504px;width:806px;height:166px;background:var(--white);border-radius:10px}
.deadline{left:34px;top:512px;width:116px;height:150px;background:var(--orange);border-radius:10px;color:var(--white);text-align:center;padding-top:8px}
.deadline .label{font-weight:900;font-size:20px;background:var(--white);color:var(--orange);margin:0 8px;border-radius:4px}
.deadline .year{font-size:16px;font-weight:700;margin-top:6px}
.deadline .date{font-size:36px;font-weight:900;line-height:1}
.deadline .until{font-size:18px;font-weight:700}
.deadline .note{font-size:10px}
.regular{left:170px;top:510px;font-size:20px;font-weight:700;line-height:36px;white-space:nowrap}
.regular strong{font-size:28px;font-weight:900;text-decoration:line-through;text-decoration-color:var(--pink)}
.price{left:166px;top:550px;width:400px;height:108px;background:var(--sky);border-radius:8px;color:var(--blue);font-weight:900;font-size:94px;line-height:104px;padding-left:24px;letter-spacing:-2px;overflow:hidden}
.price .yen{font-size:42px;margin-left:8px}
.price .tax{position:absolute;right:14px;top:14px;font-size:16px;background:var(--white);color:var(--blue);border-radius:50%;width:44px;height:44px;line-height:44px;text-align:center;letter-spacing:0}
.offer{left:584px;top:514px;width:230px}
.offer .target{font-size:14px;font-weight:700;color:var(--navy);text-align:center}
.offer .limited{display:flex;align-items:center;justify-content:center;gap:6px;color:var(--pink);font-weight:900;font-size:22px}
.offer .limited .first{background:var(--pink);color:var(--white);font-size:14px;border-radius:50%;width:34px;height:34px;line-height:34px;text-align:center}
.offer .limited .num{font-size:38px;line-height:1.1}
.free-list{left:590px;top:588px;display:flex;gap:8px}
.free{width:68px;height:68px;border-radius:50%;background:var(--blue);color:var(--white);font-size:12px;font-weight:700;text-align:center;display:flex;align-items:center;justify-content:center;line-height:1.3}

/* scope */
.scope-bar{left:20px;top:694px;width:520px;height:46px;background:var(--pink);color:var(--white);font-weight:900;font-size:28px;line-height:46px;padding-left:20px;border-radius:4px}
.scope-bar em{font-style:normal;color:var(--yellow)}
.pro-bubble{left:600px;top:694px;width:118px;height:56px;border:2px solid var(--blue);border-radius:28px;font-size:14px;font-weight:700;color:var(--blue);text-align:center;display:flex;align-items:center;justify-content:center;line-height:1.3;background:var(--white);z-index:1}
.worker-illust{left:700px;top:740px;width:126px;height:196px;background:linear-gradient(180deg,#bfe3f5,#7fc3e6);border-radius:8px}

.steps-box{left:20px;top:752px;width:300px;height:184px;border:3px solid var(--blue);border-radius:10px;padding:6px 12px}
.steps-box .title{display:inline-block;background:var(--blue);color:var(--white);font-weight:700;font-size:14px;padding:1px 10px;border-radius:10px}
.steps-box .lead{color:var(--pink);font-weight:900;font-size:21px;line-height:1.3;margin-top:2px}
.steps-box .desc{font-size:11px;line-height:1.4;margin-top:2px}
.step-photos{display:flex;gap:6px;margin-top:5px}
.step-photo{width:86px;height:50px;background:linear-gradient(135deg,#c9ced4,#8e979f);border-radius:4px}
.step-captions{display:flex;gap:6px;font-size:10px;line-height:1.5;margin-top:2px}
.step-captions span{width:86px}

.time-badge{left:334px;top:760px;width:74px;height:92px;border:2px solid var(--blue);border-radius:8px;text-align:center;color:var(--blue);font-size:12px;font-weight:700;padding-top:6px}
.time-badge .hours{background:var(--blue);color:var(--white);font-size:18px;font-weight:900;margin:4px 6px;border-radius:4px;line-height:1.2;padding:2px 0}
.house-illust{left:418px;top:756px;width:276px;height:176px;background:linear-gradient(180deg,#eef7fc,#d2ebf8);border-radius:8px}
.room{position:absolute;background:var(--pink);color:var(--white);font-size:14px;font-weight:700;padding:1px 10px;border-radius:12px}

.notes{left:20px;top:944px;width:806px;font-size:11px;color:var(--gray);line-height:1.5}

/* contact */
.contact{left:0;top:990px;width:846px;height:210px;background:var(--blue-dark)}
.tel-label{left:30px;top:1004px;color:var(--white);font-weight:700;font-size:22px}
.tel-box{left:30px;top:1042px;width:400px;height:70px;background:var(--white);border-radius:8px;display:flex;align-items:center;gap:10px;padding-left:16px}
.tel-box .num{color:var(--navy);font-weight:900;font-size:44px;letter-spacing:1px;white-space:nowrap}
.hours{left:30px;top:1120px;color:var(--white);font-size:13px}
.id-box{left:300px;top:1118px;border:1px solid var(--white);color:var(--white);font-size:13px;padding:1px 8px;width:130px}
.web-label{left:470px;top:1004px;width:250px;background:var(--white);color:var(--blue-dark);font-weight:700;font-size:19px;text-align:center;border-radius:16px;padding:2px 0}
.search{left:470px;top:1046px;width:250px;height:36px;display:flex}
.search .field{flex:1;background:var(--white);border-radius:4px 0 0 4px;font-size:16px;font-weight:700;line-height:36px;padding-left:10px}
.search .btn{width:56px;background:var(--navy);color:var(--white);font-size:14px;font-weight:700;text-align:center;line-height:36px;border-radius:0 4px 4px 0}
.company{left:470px;top:1092px;color:var(--white);font-weight:700;font-size:20px}
.qr-slot{left:734px;top:1004px;width:90px;height:150px;background:var(--white);border-radius:10px;padding:10px}
.qr-slot .label{font-size:10px;text-align:center;font-weight:700;color:var(--navy)}
.qr-slot .area{margin-top:6px;width:70px;height:70px;border:2px dashed var(--gray)}
</style>
</head>
<body>
<div class="flyer">

  <div class="abs hero-photo" role="img" aria-label="排水口の臭いに鼻をつまむ女性の写真"></div>
  <div class="abs worries">
    <p class="worry">台所の排水口から悪臭がする…</p>
    <p class="worry">洗面台の排水口が臭う…</p>
    <p class="worry">家の中がなんだか下水臭い…</p>
  </div>

  <div class="abs headline-band"></div>
  <p class="abs tag-smell">その悪臭！！</p>
  <h1 class="abs headline">排水管の<span class="dirty">汚れ</span>が原因</h1>
  <p class="abs headline-sub">かもしれません！</p>

  <div class="abs campaign"></div>
  <p class="abs campaign-banner">＼ 今なら超おトク！地域一斉清掃キャンペーン開催！ ／</p>
  <h2 class="abs campaign-pill">排水管のお掃除しませんか？</h2>
  <div class="abs price-panel"></div>

  <div class="abs deadline">
    <p class="label">期間限定</p>
    <p class="year">2023</p>
    <p class="date">12/31</p>
    <p class="until">まで</p>
    <p class="note">お申込みは当日まで</p>
  </div>

  <p class="abs regular">通常価格 <strong>25,000円</strong> が今だけ！</p>
  <p class="abs price">5,000<span class="yen">円</span><span class="tax">税込</span></p>

  <div class="abs offer">
    <p class="target">戸建住宅にお住まいの方</p>
    <p class="limited"><span class="first">先着</span><span class="num">30</span>名様限定</p>
  </div>
  <div class="abs free-list">
    <p class="free">見積費用<br>一切なし</p>
    <p class="free">出張費用<br>一切なし</p>
    <p class="free">追加料金<br>一切なし</p>
  </div>

  <h2 class="abs scope-bar">洗浄範囲は<em>お家一軒丸ごと！</em></h2>
  <div class="abs worker-illust" role="img" aria-label="作業着姿で洗浄ホースを持つ作業員のイラスト"></div>
  <p class="abs pro-bubble">プロの<br>お掃除技術！</p>

  <div class="abs steps-box">
    <span class="title">お掃除の手順</span>
    <p class="lead">水圧の力で徹底洗浄！</p>
    <p class="desc">専用の機械で排水管の奥まで高圧洗浄し、こびりついた汚れを一気に落とします。</p>
    <div class="step-photos">
      <div class="step-photo" role="img" aria-label="汚水マスを開ける作業の写真"></div>
      <div class="step-photo" role="img" aria-label="高圧洗浄の作業写真"></div>
      <div class="step-photo" role="img" aria-label="洗浄後の確認作業の写真"></div>
    </div>
    <div class="step-captions"><span>①汚水マス開け</span><span>②高圧洗浄</span><span>③仕上げ確認</span></div>
  </div>

  <div class="abs time-badge">作業時間<p class="hours">2時間</p>程度</div>

  <div class="abs house-illust" role="img" aria-label="キッチン・お風呂・洗面所・トイレの排水管がつながる家の断面イラスト">
    <span class="room" style="left:20px;top:14px">キッチン</span>
    <span class="room" style="left:170px;top:14px">お風呂</span>
    <span class="room" style="left:20px;top:140px">洗面所</span>
    <span class="room" style="left:180px;top:140px">トイレ</span>
  </div>

  <p class="abs notes">※作業時間は排水管の状況や建物の構造により異なります。※集合住宅は対象外となります。※ご予約状況により、ご希望の日程に添えない場合がございます。</p>

  <div class="abs contact"></div>
  <p class="abs tel-label">▶ お電話からのお申込はこちら</p>
  <div class="abs tel-box">
    <svg width="40" height="40" viewBox="0 0 24 24" aria-hidden="true"><path fill="#0b3f7a" d="M6.6 10.8a15.1 15.1 0 0 0 6.6 6.6l2.2-2.2a1 1 0 0 1 1-.25 11.4 11.4 0 0 0 3.6.57 1 1 0 0 1 1 1V20a1 1 0 0 1-1 1A17 17 0 0 1 3 4a1 1 0 0 1 1-1h3.5a1 1 0 0 1 1 1c0 1.25.2 2.45.57 3.6a1 1 0 0 1-.25 1z"/></svg>
    <span class="num">0120-000-000</span>
  </div>
  <p class="abs hours">受付時間：平日9:00〜18:00（土日祝除く）</p>
  <p class="abs id-box">識別番号 000</p>

  <p class="abs web-label">24時間ネット申込はこちら</p>
  <div class="abs search"><span class="field">株式会社〇〇〇〇〇</span><span class="btn">検索</span></div>
  <p class="abs company">株式会社〇〇〇〇〇</p>
  <div class="abs qr-slot">
    <p class="label">QRコードで<br>かんたん申込</p>
    <div class="area"></div>
  </div>

</div>
</body>
</html>
```